Calloway Aeronautics website

We are an aviation company based in Miramar, FL but with worldwide coverage. We are involved in commercial aircraft (mostly freighters) trading, sale & leasing. Specifically, we specialized in freighters of the Vantrex family (V310, V320, V330, V340, V350). We also assist with financing, sale/leaseback. Handle special aviation projects and provide consultancy services. Currently engaged in a Vantrex 350 passenger to Freighter conversion (P2F).

Website Preliminary Initial Content/Sections as follows:

About Us
Founded in 2011, Calloway Aeronautics' management has many years of experience in Aviation, a strong background in scheduled airlines with emphasis in all cargo operations, freight forwarding supply chain and freight logistics, as well as ACMI and CMI operations.

Calloway’s focuses in facilitating wet and dry lease operations, charter and ACMI programs consultancy, aircraft sales, leasing and procurement, aviation consultancy and aircraft management.

Calloway team is a hands-on reliable alternative that works toward achieving your aircraft and aviation objectives by meeting your requirements and timeframe throughout professional and personalized service.

Teodoro Lasalle has over three decades of experience in the aviation field including aircraft maintenance, airline management, supply chain and logistics management. Teodoro is a true entrepreneur with proven experience and expertise on the multiple facets of the commercial aviation industry throughout the creation and development of a cluster of aviation entities. Teodoro is the founder and former sole member/chairman of 64 Jet, a Vantrex 340 All-Cargo U.S. Certificated Air Carrier created from scratch in 2014 which nowadays conforms a superb growing airline platform with an immaculate compliance operational record.

Services

Aircraft Finance, Trading, Procurement and Leasing
Calloway buys, sells, leases and facilitates aircraft trading while specializes in structured aircraft investment projects. Calloway has deep industry relationships and years of expertise, allowing to successfully execute lease transactions. We assist airlines, financial institutions and leasing companies when selling or purchasing aircraft.

Aircraft Available for Sale/Lease

Sale/Leaseback
Sale-leaseback is a method of financing. If your company needs liquidity, your aircraft or engine can serve as collateral for a loan throughout a sale-leaseback transaction. Sale-leaseback can free the equity tied up in aircraft or asset. Even if there is no pressing need for funds, a sale-leaseback allows you to use the equity tied up in your aircraft in a more productive fashion. Leaseback arrangements are usually employed because they confer financing, accounting or taxation benefits.

Passenger to Freighter Conversion (P2F)
Pandemic has seen the resurgence of operators packing freight into the main cabins of passenger aircraft. Carriers have been allowed to transport cargo in the cabin by removing passenger seats completely. NCA/ORSA have established exemptions that allow operators to fly in “Preighter” configuration for a limited time. Calloway is closely working with a U.S. group that is developing a Class E Supplemental Type Certificate (STC) for applicability on V350 aircraft which will include a cargo door for containerized freight. Final approvals are expected during first quarter of 2022.
Wet lease
Throughout our deep relationships within the industry, Calloway facilitates short or long-term wet leases to airlines and qualified parties around the globe, whereby we provide the Aircraft, Crews, Maintenance and Insurance (ACMI) worldwide services at competitive rates. We also specialize in AM leases where the aircraft is registered onto Lessee´s AOC with all maintenance services included in the rates, covering all maintenance risks, or CM or CMI where the client provides the aircraft.

Dry Lease
We offer aircraft from our own portfolio on dry lease or could engage in procuring the aircraft of your choice.

Asset & Aircraft Management
We provide aircraft owners Aircraft Management services, where we manage the technical side of the aircraft or the asset. Calloway also provides Harwick Dynamo engines trading, repair and full management services. We also buy Vantrex/Skylane surplus inventory.

Worldwide Charters
We facilitate the arrangement of full charters to airlines and logistics companies. Certain territory restrictions may apply.

Aviation Consultancy
We provide airline consultancy services for new or special projects. Calloway also specializes on All Cargo International route analysis, implementation and development. Our team provides professional guidance in obtaining worldwide both scheduled and charter authority.

Target Market(s)

Our target market are the airlines, logistics companies and commercial aviation related entities

Industry/Entity Type

Commercial Aviation

Coding

Number of Pages Required

3 page

Requirements
Must have
• Illustrations of wide body freighters such V350, V340, V320

```html
<!DOCTYPE html>
<html lang="en">
<head>
<meta charset="utf-8">
<title>Calloway Aeronautics</title>
<link href="https://fonts.googleapis.com/css2?family=Lato:wght@400;700;900&display=swap" rel="stylesheet">
<style>
:root{
  --navy:#0c1a4b;
  --navy-deep:#08123a;
  --orange:#ef8b0f;
  --orange-soft:rgba(239,139,15,0.55);
  --white:#ffffff;
  --ink:#1d1d1d;
  --muted:#6b6b6b;
  --grey-bg:#ececec;
  --footer:#1c1f27;
}
*{box-sizing:border-box;margin:0;padding:0}
html,body{width:1200px;height:3066px;overflow:hidden}
body{font-family:'Lato',sans-serif;color:var(--ink);background:var(--white);position:relative}
.abs{position:absolute}
a{color:inherit;text-decoration:none}

/* header */
.site-header{position:absolute;left:0;top:0;width:1200px;height:84px;background:var(--navy);z-index:3}
.brand{position:absolute;left:90px;top:16px;color:var(--white);text-align:center;width:176px}
.brand-name{font-size:26px;letter-spacing:1px;font-weight:400;line-height:30px}
.brand-sub{font-size:12px;letter-spacing:11px;line-height:16px;padding-left:8px}
.main-nav a{position:absolute;top:31px;color:var(--white);font-size:15px}
.main-nav a.active{color:var(--orange);text-decoration:underline}
.btn-inquiry{position:absolute;left:984px;top:24px;width:128px;height:36px;background:var(--orange);color:var(--white);font-size:15px;font-weight:700;text-align:center;line-height:36px}

/* hero */
.hero{position:absolute;left:0;top:84px;width:1200px;height:460px}
.hero-title{position:absolute;left:0;width:1200px;top:136px;text-align:center;color:var(--white);font-size:52px;font-weight:700}
.hero-sub{position:absolute;left:0;width:1200px;top:189px;text-align:center;color:var(--white);font-size:19px}
.btn-ghost-light{position:absolute;left:519px;top:230px;width:162px;height:38px;border:2px solid var(--white);color:var(--white);font-size:14px;text-align:center;line-height:34px}
.hero-ornament{position:absolute;left:268px;top:388px;width:664px;height:62px;background:linear-gradient(90deg,rgba(239,139,15,0) 0%,var(--orange-soft) 30%,var(--orange) 50%,var(--orange-soft) 70%,rgba(239,139,15,0) 100%)}

/* about */
.section-title{font-size:33px;font-weight:900;color:var(--orange)}
.about-title{position:absolute;left:88px;top:618px}
.about-copy{position:absolute;left:88px;top:678px;width:510px;font-size:14.5px;line-height:19.3px}
.about-copy p{margin-bottom:19px}
.btn-outline{position:absolute;border:2px solid var(--orange);color:var(--orange);font-size:15px;text-align:center;background:var(--white)}
.about-bar{position:absolute;left:702px;top:637px;width:16px;height:376px;background:var(--orange)}
.about-photo{position:absolute;left:718px;top:587px;width:394px;height:426px;background:linear-gradient(135deg,#c9d3dd 0%,#8fa3b6 45%,#3b4656 80%,#7a3a2e 100%)}
.founded{position:absolute;left:673px;top:838px;width:107px;height:99px;background:var(--navy);border:4px solid var(--white);color:var(--white);text-align:center;padding-top:14px}
.founded small{display:block;font-size:14px}
.founded strong{display:block;font-size:36px;font-weight:700;line-height:40px}

/* services */
.services-bg{position:absolute;left:0;top:1086px;width:1200px;height:690px}
.services-title{position:absolute;left:0;width:1200px;top:1164px;text-align:center;color:var(--white);font-size:33px;font-weight:900}
.service-card{position:absolute;top:1238px;width:325px;height:368px;background:var(--white)}
.service-card .card-image{height:176px}
.service-card h3{position:absolute;left:24px;top:196px;width:290px;font-size:19px;line-height:22px;font-weight:400;color:var(--orange)}
.service-card p{position:absolute;left:24px;top:250px;width:285px;font-size:14px;line-height:20px;color:var(--muted)}
.service-card .btn-outline{left:24px;top:310px;width:124px;height:36px;line-height:32px}
.service-card .btn-outline.filled{background:var(--orange);color:var(--white)}
.btn-ghost-white{position:absolute;left:548px;top:1646px;width:104px;height:38px;border:2px solid var(--white);color:var(--white);font-size:15px;font-weight:700;text-align:center;line-height:34px}

/* testimonials */
.testimonials-title{position:absolute;left:0;width:1200px;top:1843px;text-align:center}
.quote-badge{position:absolute;left:576px;top:1908px;width:48px;height:48px;border-radius:50%;background:var(--orange)}
.testimonial-text{position:absolute;left:230px;width:740px;top:1979px;text-align:center;font-size:14.5px;line-height:20px}
.testimonial-author{position:absolute;left:0;width:1200px;top:2052px;text-align:center;font-size:15px;color:var(--orange)}
.testimonial-author span{color:var(--navy);font-size:12px;margin-left:4px}

/* inquiry */
.inquiry-bg{position:absolute;left:0;top:2216px;width:1200px;height:478px}
.inquiry-title{position:absolute;left:0;width:1200px;top:2309px;text-align:center}
.field{position:absolute;background:var(--white);border:1px solid #d9d9d9;font-size:12.5px;color:var(--muted);padding-left:31px;line-height:42px}
.field svg{position:absolute;left:10px;top:14px}
.field.area{line-height:20px;padding-top:10px}
.field.area svg{top:13px}
.btn-submit{position:absolute;left:545px;top:2574px;width:110px;height:40px;background:var(--orange);color:var(--white);font-weight:700;font-size:15px;text-align:center;line-height:40px}

/* footer */
.site-footer{position:absolute;left:0;top:2694px;width:1200px;height:330px;background:linear-gradient(120deg,#252a35 0%,#171a22 55%,#232b3a 100%)}
.footer-heading{position:absolute;font-size:18px;font-weight:700;color:var(--orange)}
.quick-links a{position:absolute;left:88px;color:var(--white);font-size:14.5px}
.quick-links a.active{color:var(--orange);text-decoration:underline}
.contact-row{position:absolute;left:342px;color:var(--white);font-size:14.5px;line-height:20px}
.contact-icon{position:absolute;left:313px}
.map-area{position:absolute;left:712px;top:2776px;width:400px;height:182px;background:linear-gradient(135deg,#f3f1ec,#e5e8ec)}
.bottom-bar{position:absolute;left:0;top:3024px;width:1200px;height:42px;background:var(--orange)}
.copyright{position:absolute;left:88px;top:12px;color:var(--white);font-size:14px}
.social{position:absolute;top:16px;width:11px;height:11px;border-radius:50%;background:var(--white)}
</style>
</head>
<body>

<header class="site-header">
  <div class="brand"><div class="brand-name">CALLOWAY</div><div class="brand-sub">AERONAUTICS</div></div>
  <nav class="main-nav">
    <a class="active" style="left:533px">Home</a>
    <a style="left:600px">About Us</a>
    <a style="left:687px">Services</a>
    <a style="left:767px">Testimonials</a>
    <a style="left:874px">Contact Us</a>
  </nav>
  <a class="btn-inquiry">Quick Inquiry</a>
</header>

<section class="hero">
  <svg class="abs" style="left:0;top:0" width="1200" height="460" viewBox="0 0 1200 460">
    <defs>
      <linearGradient id="heroFill" x1="0" y1="0" x2="1" y2="1">
        <stop offset="0" stop-color="#8a8f97"/>
        <stop offset="0.45" stop-color="#3d4656"/>
        <stop offset="0.75" stop-color="#2b3f66"/>
        <stop offset="1" stop-color="#4a4740"/>
      </linearGradient>
    </defs>
    <path d="M0 0H1200V374Q600 470 0 374Z" fill="url(#heroFill)" role="img" aria-label="Engineers servicing a jet engine in a hangar"/>
    <path d="M0 0H1200V374Q600 470 0 374Z" fill="#000" opacity="0.25"/>
  </svg>
  <div class="hero-ornament" role="img" aria-label="Orange winged star divider ornament"></div>
  <h1 class="hero-title">Trading</h1>
  <div class="hero-sub">Buying or selling aircraft, smoothly handled</div>
  <a class="btn-ghost-light">View Full Details</a>
</section>

<section>
  <h2 class="section-title about-title">About Us</h2>
  <div class="about-copy">
    <p>Founded in 2011, Calloway Aeronautics' management has many years of experience in Aviation, a strong background in scheduled airlines with emphasis in all cargo operations, freight forwarding supply chain and freight logistics, as well as ACMI and CMI operations.</p>
    <p>Calloway’s focuses in facilitating wet and dry lease operations, charter and ACMI programs consultancy, aircraft sales, leasing and procurement, aviation consultancy and aircraft management.</p>
    <p>Calloway team is a hands-on reliable alternative that works toward achieving your aircraft and aviation objectives by meeting your requirements and timeframe throughout professional and personalized service.</p>
  </div>
  <a class="btn-outline" style="left:88px;top:937px;width:140px;height:38px;line-height:34px">Learn More</a>
  <div class="about-bar"></div>
  <div class="about-photo" role="img" aria-label="Two technicians inspecting a large jet engine"></div>
  <div class="founded"><small>Founded in</small><strong>2011</strong></div>
</section>

<section>
  <svg class="services-bg" viewBox="0 0 1200 690" role="img" aria-label="Dark navy aviation backdrop">
    <path d="M0 78 L600 0 L1200 78 V607 L600 688 L0 607Z" fill="#0c1a4b"/>
  </svg>
  <h2 class="services-title">Services</h2>
  <svg class="abs" style="left:47px;top:1400px" width="18" height="46"><path d="M16 1 L2 23 L16 45" fill="none" stroke="#8b95b5" stroke-width="1.5"/></svg>
  <svg class="abs" style="left:1136px;top:1400px" width="18" height="46"><path d="M2 1 L16 23 L2 45" fill="none" stroke="#ef8b0f" stroke-width="1.5"/></svg>

  <article class="service-card" style="left:88px">
    <div class="card-image" role="img" aria-label="Model airliner resting on a calculator" style="background:linear-gradient(135deg,#e9e9e9,#9a9a9a 60%,#3a3a3a)"></div>
    <h3>Aircraft Finance, Trading,<br>Procurement and Leasing</h3>
    <p>Calloway buys, sells, leases and facilitates aircraft trading while specializes in...</p>
    <a class="btn-outline">Learn More</a>
  </article>
  <article class="service-card" style="left:438px">
    <div class="card-image" role="img" aria-label="Business jet parked in a hangar" style="background:linear-gradient(135deg,#d7d7d7,#8a8a8a 55%,#2e2e2e)"></div>
    <h3>Aircraft Available for Sale/Lease<br>Sale/Leaseback</h3>
    <p>Sale-leaseback is a method of financing. If your company needs liquidity, your...</p>
    <a class="btn-outline">Learn More</a>
  </article>
  <article class="service-card" style="left:787px">
    <div class="card-image" role="img" aria-label="Container cargo ship at sea from above" style="background:linear-gradient(135deg,#3fb4c7,#1f7f98 55%,#145e75)"></div>
    <h3>Passenger to Freighter<br>Conversion (P2F)</h3>
    <p>Calloway buys, sells, leases and facilitates aircraft trading while specializes in...</p>
    <a class="btn-outline filled">Learn More</a>
  </article>
  <a class="btn-ghost-white">View All</a>
</section>

<section>
  <h2 class="section-title testimonials-title">Testimonials</h2>
  <div class="quote-badge">
    <svg width="48" height="48" viewBox="0 0 48 48"><path d="M14 30 V24 Q14 17 21 15 L22 18 Q18 19 18 23 H22 V30Z M26 30 V24 Q26 17 33 15 L34 18 Q30 19 30 23 H34 V30Z" fill="#fff"/></svg>
  </div>
  <svg class="abs" style="left:128px;top:1986px" width="18" height="46"><path d="M16 1 L2 23 L16 45" fill="none" stroke="#9a9a9a" stroke-width="1.5"/></svg>
  <svg class="abs" style="left:1050px;top:1986px" width="18" height="46"><path d="M2 1 L16 23 L2 45" fill="none" stroke="#ef8b0f" stroke-width="1.5"/></svg>
  <p class="testimonial-text">Lorem Ipsum is simply dummy text of the printing and typesetting industry. Lorem Ipsum has been the industry's standard dummy text ever since the 1500s, when an unknown printer took a galley of type and scrambled it to make a type specimen book. It has survived not only five centuries, but also the leap into...</p>
  <div class="testimonial-author">Maren Holloway <span>Simply Beautiful</span></div>
  <a class="btn-outline" style="left:531px;top:2110px;width:137px;height:40px;line-height:36px">Learn More</a>
</section>

<section>
  <svg class="inquiry-bg" viewBox="0 0 1200 478"><path d="M0 111 L600 0 L1200 111 V478 H0Z" fill="#ececec"/></svg>
  <h2 class="section-title inquiry-title">Quick Inquiry</h2>
  <div class="field" style="left:126px;top:2381px;width:304px;height:38px;line-height:36px">
    <svg width="13" height="13" viewBox="0 0 13 13" style="top:12px"><circle cx="6.5" cy="4" r="3" fill="none" stroke="#ef8b0f" stroke-width="1.2"/><path d="M1 12.5 Q6.5 5 12 12.5" fill="none" stroke="#ef8b0f" stroke-width="1.2"/></svg>Name</div>
  <div class="field" style="left:448px;top:2381px;width:303px;height:38px;line-height:36px">
    <svg width="14" height="11" viewBox="0 0 14 11" style="top:13px"><rect x="0.6" y="0.6" width="12.8" height="9.8" fill="none" stroke="#ef8b0f" stroke-width="1.2"/><path d="M1 1 L7 6 L13 1" fill="none" stroke="#ef8b0f" stroke-width="1.2"/></svg>Email</div>
  <div class="field" style="left:769px;top:2381px;width:304px;height:38px;line-height:36px">
    <svg width="9" height="14" viewBox="0 0 9 14" style="top:12px"><rect x="0.6" y="0.6" width="7.8" height="12.8" rx="1.5" fill="none" stroke="#ef8b0f" stroke-width="1.2"/></svg>Phone</div>
  <div class="field area" style="left:126px;top:2436px;width:947px;height:104px">
    <svg width="13" height="13" viewBox="0 0 13 13"><path d="M0.6 0.6 H12.4 V8 L8 12.4 H0.6Z" fill="none" stroke="#ef8b0f" stroke-width="1.2"/></svg>How can we help?</div>
  <a class="btn-submit">Submit</a>
</section>

<footer class="site-footer" role="img" aria-label="Darkened hangar photo behind the footer">
</footer>
<div class="footer-heading" style="left:88px;top:2771px">Quick Link</div>
<nav class="quick-links">
  <a class="active" style="top:2808px">Home</a>
  <a style="top:2841px">About Us</a>
  <a style="top:2874px">Services</a>
  <a style="top:2907px">Testimonials</a>
  <a style="top:2940px">Contact Us</a>
</nav>
<div class="footer-heading" style="left:313px;top:2774px">Conatct info</div>
<svg class="contact-icon" style="top:2822px" width="16" height="20" viewBox="0 0 16 20"><path d="M8 0 C3.6 0 0.5 3.2 0.5 7.3 C0.5 12.5 8 20 8 20 C8 20 15.5 12.5 15.5 7.3 C15.5 3.2 12.4 0 8 0Z" fill="#ef8b0f"/><circle cx="8" cy="7.3" r="2.8" fill="#1c1f27"/></svg>
<div class="contact-row" style="top:2818px">Lorem Ipsum<br>Suite 12, 48 Harbor Crest Drive,<br>Bayview, FL, 33025</div>
<svg class="contact-icon" style="top:2897px" width="15" height="15" viewBox="0 0 15 15"><path d="M3 0.5 L5.5 3.5 L4 5.5 Q5.5 9 9.5 11 L11.5 9.5 L14.5 12 L12.5 14.5 Q5 13.5 0.5 3Z" fill="#ef8b0f"/></svg>
<div class="contact-row" style="top:2894px">0400 555 018</div>
<svg class="contact-icon" style="top:2938px" width="16" height="12" viewBox="0 0 16 12"><rect width="16" height="12" fill="#ef8b0f"/><path d="M0.5 0.5 L8 7 L15.5 0.5" fill="none" stroke="#1c1f27" stroke-width="1.2"/></svg>
<div class="contact-row" style="top:2933px">info@callowayaero.example</div>
<div class="map-area" role="img" aria-label="Street map showing the office location"></div>

<div class="bottom-bar">
  <div class="copyright">Copyright © 2021 Calloway Aeronautics. All Rights Reserved</div>
  <span class="social" style="left:1005px"></span>
  <span class="social" style="left:1035px"></span>
  <span class="social" style="left:1067px"></span>
  <span class="social" style="left:1099px"></span>
</div>

</body>
</html>
```